Chicago based record lable needs Cd cover design for single. Imagination welcomed.

Cd cover design for single "Paper Crowns". As the old saying goes, don't work don't eat. (Eat meaning making money) Smorgasbord, elegant dinning setting, ballroom dinning, anything related to eating and eating good. A feast if you will. No specific colors in mind. We like out of the ordinary. “Get Creative”. Artist: Rik Marlowe

```html
<!DOCTYPE html>
<html lang="en">
<head>
<meta charset="utf-8">
<title>Paper Crowns — Rik Marlowe</title>
<link href="https://fonts.googleapis.com/css2?family=Oswald:wght@400&family=Open+Sans:wght@600&family=Kaushan+Script&display=swap" rel="stylesheet">
<style>
  :root {
    --backdrop: #e4e4e4;
    --cover-red: #8e1a1f;
    --cover-wine: #6a1f3a;
    --cover-plum: #4a2a5e;
    --cover-navy: #2c2b5c;
    --bowl-dark: #2a2436;
    --food-warm: #8a4a2e;
    --food-green: #3f6b3a;
    --type-white: #ffffff;
  }
  * { margin: 0; padding: 0; box-sizing: border-box; }
  html, body {
    width: 1200px;
    height: 854px;
    overflow: hidden;
    background: var(--backdrop);
  }
  .stage {
    position: relative;
    width: 1200px;
    height: 854px;
  }
  .cover {
    position: absolute;
    left: 200px;
    top: 27px;
    width: 800px;
    height: 800px;
    overflow: hidden;
  }
  .cover-photo {
    position: absolute;
    inset: 0;
    background:
      radial-gradient(circle at 52% 56%, var(--food-green) 0%, var(--food-warm) 22%, var(--bowl-dark) 42%, transparent 58%),
      linear-gradient(180deg, var(--cover-red) 0%, var(--cover-wine) 35%, var(--cover-plum) 65%, var(--cover-navy) 100%);
  }
  .artist-name {
    position: absolute;
    top: 56px;
    left: 0;
    width: 100%;
    text-align: center;
    font-family: "Oswald", sans-serif;
    font-weight: 400;
    font-size: 21px;
    letter-spacing: 21px;
    text-indent: 21px;
    color: var(--type-white);
    text-transform: uppercase;
  }
  .title-lead {
    position: absolute;
    top: 280px;
    left: 0;
    width: 100%;
    text-align: center;
    font-family: "Open Sans", sans-serif;
    font-weight: 600;
    font-size: 44px;
    letter-spacing: 22px;
    text-indent: 22px;
    color: var(--type-white);
    text-transform: uppercase;
  }
  .title-script {
    position: absolute;
    top: 320px;
    left: 0;
    width: 100%;
    text-align: center;
    font-family: "Kaushan Script", cursive;
    font-size: 170px;
    line-height: 1.2;
    color: var(--type-white);
  }
</style>
</head>
<body>
  <main class="stage">
    <section class="cover">
      <div class="cover-photo" role="img" aria-label="Overhead photo of a rustic bowl of chickpeas, flatbread, olives, peppers and greens on a wooden table, tinted red to purple"></div>
      <p class="artist-name">Rik Marlowe</p>
      <h1>
        <span class="title-lead">Paper</span>
        <span class="title-script">Crowns</span>
      </h1>
    </section>
  </main>
</body>
</html>
```